Improving a camping website homepage header*

My client is very happy with his new website and its new functionalities. However, he's not very happy about the homepage design. Specifically, the header(this includes the menu, large header image and two columns beneath that). You can find the website here: http://lnkvo.example/siteTentra .

He forwarded me several other websites he likes. Which can be found in the attachments. I also included several pictures of the camping.

I'm looking for a design that will improve the header of the homepage with room for other global style chances. The logo cannot be changed.

Attachments
1) His old website homepage
2) Website mockup he liked.
3) Another website mockup he liked.

Other images can be found on the new website http://lnkvo.example/siteTentra or his old website http://lnkvo.example/formerSiteTentra.

Can you help us?
Updates

Hello guys. Here's a bit more information - Language used on the website is dutch. - The two columns left/right are supposed to link to Hire/Buy chalets. The client indicated that he finds these links important, but doesn't like the current design. I think this is partially the case because he doesn't like the icons. I'm looking forward to your designs!

Target Market(s)

30-50 year old wealthy people that want to purchase or rent cabins in the Netherlands.

Number of Pages Required

1 page

Colors

Designer to choose colors to be used in the design.

Requirements
Must have
• Improved header
Nice to have
• Global style changes
Should not have
• Logo changes

```html
<!DOCTYPE html>
<html lang="nl">
<head>
<meta charset="utf-8">
<title>Parc Veldhoeve</title>
<link href="https://fonts.googleapis.com/css2?family=Montserrat:wght@600;700;800&family=Open+Sans:wght@400;600&display=swap" rel="stylesheet">
<style>
:root{
  --orange:#ff7e00;
  --green:#5a9e1f;
  --sky:#2f8fe0;
  --panel:#f1f1f1;
  --ink:#222;
  --body:#444;
  --footer:#2b2f36;
  --footer-bar:#24272d;
  --line:#e2e2e2;
}
*{box-sizing:border-box;margin:0;padding:0}
html,body{width:806px;height:1200px;overflow:hidden;background:#fff}
body{position:relative;font-family:"Open Sans",sans-serif;color:var(--body)}
.abs{position:absolute}
.hero{left:0;top:0;width:806px;height:395px;background:linear-gradient(180deg,#1f7fe0 0%,#7cc0f0 40%,#8c9a6a 62%,#6ea23a 75%,#4f8a22 100%)}
.brand{left:90px;top:18px;display:flex;align-items:center;gap:8px}
.brand-mark{width:16px;height:16px;border-radius:50%;background:#fff}
.brand-name{font-size:18px;font-weight:600;color:#fff;line-height:1}
.call{left:482px;top:12px;color:#fff;font-family:Montserrat,sans-serif;display:flex;align-items:center;gap:6px}
.call small{font-size:7.5px;font-weight:700}
.call b{font-size:12px;font-weight:800}
.social-top{left:660px;top:14px;display:flex;gap:15px}
.social-top span{width:9px;height:9px;border-radius:50%;background:#fff}
.nav{left:347px;top:39px;display:flex;font-family:Montserrat,sans-serif;font-size:7.5px;font-weight:700;color:#fff}
.nav a{color:#fff;text-decoration:none;padding:5px 8px}
.nav a.active{background:var(--orange)}
.hero-title{left:0;width:806px;top:299px;text-align:center;font-family:Montserrat,sans-serif;font-weight:800;font-size:18px;color:#fff;text-transform:uppercase}
.btn{background:var(--orange);color:#fff;font-family:Montserrat,sans-serif;font-weight:700;text-transform:uppercase;text-align:center}
.hero-btn{left:364px;top:336px;width:78px;height:23px;line-height:19px;font-size:8px;border:2px solid #fff}
.dots{left:706px;top:186px;display:flex;flex-direction:column;gap:6px}
.dots span{width:4px;height:4px;border-radius:50%;background:#fff}
.dots span.on{background:var(--orange);box-shadow:0 0 0 1.5px #fff}
.welcome{left:6px;top:401px;width:389px;height:239px;background:var(--panel)}
.welcome h3{position:absolute;left:83px;top:40px;font-family:Montserrat,sans-serif;font-size:11px;font-weight:700;color:var(--ink)}
.welcome h2{position:absolute;left:82px;top:57px;font-family:Montserrat,sans-serif;font-size:20px;font-weight:800;color:var(--green)}
.welcome p{position:absolute;left:83px;top:100px;width:225px;font-size:7.4px;line-height:11.8px;color:var(--body)}
.welcome .btn{position:absolute;left:85px;top:182px;width:56px;height:16px;line-height:16px;font-size:6.5px}
.welcome-photo{left:396px;top:401px;width:406px;height:239px;background:linear-gradient(180deg,#a9c49a 0%,#5f8a3c 45%,#e6e4d8 55%,#4e7a2a 75%,#3d5a2a 100%)}
.section-title{left:108px;top:682px;font-size:15px;font-weight:400;color:#333}
.card{width:187px;height:223px;top:711px;border:1px solid var(--line);background:#fff}
.card .photo{position:absolute;left:0;top:0;width:185px;height:116px;background:linear-gradient(180deg,#8aa67a 0%,#b8b8ad 45%,#6c8a4a 100%)}
.tag{position:absolute;top:12px;font-size:6px;color:#fff;padding:1px 4px}
.tag.rec{left:12px;background:#e8a04a}
.tag.type{right:12px;background:var(--sky)}
.card h4{position:absolute;left:10px;top:128px;font-size:10px;font-weight:400;color:#333}
.price{position:absolute;left:10px;top:145px;font-size:9px;color:var(--orange)}
.note{position:absolute;left:10px;top:164px;font-size:6.5px;color:#666}
.stats{position:absolute;left:10px;font-size:6.3px;color:#777}
.more{position:absolute;right:10px;font-size:6px;color:#fff;background:#e8a04a;padding:1px 4px}
.card hr{position:absolute;left:0;top:197px;width:100%;border:0;border-top:1px solid var(--line)}
.author{position:absolute;left:10px;top:203px;display:flex;align-items:center;gap:6px;font-size:6.8px;color:#666}
.author i{width:14px;height:14px;border-radius:50%;background:#8a9a7a}
.actions{position:absolute;right:10px;top:203px;display:flex;gap:4px}
.actions span{width:14px;height:14px;border:1px solid var(--line)}
.footer{left:0;top:991px;width:806px;height:176px;background:var(--footer);color:#c8cbd0;font-size:7px}
.footer h5{position:absolute;top:27px;font-size:8px;font-weight:600;color:#fff}
.contact{position:absolute;left:105px;top:47px;line-height:12px}
.contact div{display:flex;gap:8px;margin-bottom:4px}
.contact i{flex:none;width:6px;height:6px;margin-top:3px;background:#9aa0a8}
.mini{position:absolute;left:309px;display:flex;gap:7px}
.mini .thumb{width:57px;height:37px;background:linear-gradient(180deg,#9db3c4,#7e9a5e)}
.mini em{font-style:normal;color:var(--orange);display:block;margin-top:4px}
.soc{position:absolute;left:513px;top:48px;display:grid;grid-template-columns:repeat(6,27px);row-gap:11px}
.soc span{width:16px;height:16px;border-radius:50%;border:1px solid #6b7078}
.bottom{left:0;top:1167px;width:806px;height:33px;background:var(--footer-bar);color:#9aa0a8;font-size:6.5px;padding:12px 105px}
</style>
</head>
<body>
<div class="abs hero" role="img" aria-label="Photo of a large timber house on a green lawn under a blue sky"></div>
<div class="abs brand"><span class="brand-mark"></span><span class="brand-name">Parc Veldhoeve</span></div>
<div class="abs call">
  <svg width="10" height="10" viewBox="0 0 24 24"><path fill="#fff" d="M6.6 10.8a15 15 0 0 0 6.6 6.6l2.2-2.2c.3-.3.7-.4 1-.2 1.1.4 2.3.6 3.6.6.6 0 1 .4 1 1V20c0 .6-.4 1-1 1A17 17 0 0 1 3 4c0-.6.4-1 1-1h3.5c.6 0 1 .4 1 1 0 1.3.2 2.5.6 3.6.1.3 0 .7-.2 1z"/></svg>
  <small>CALL US :</small><b>0300 - 12 34 56</b>
</div>
<div class="abs social-top"><span></span><span></span><span></span></div>
<nav class="abs nav">
  <a class="active" href="#">HOME</a><a href="#">THE PARK</a><a href="#">FINANCING</a><a href="#">CHALETS</a><a href="#">OFFERS</a><a href="#">FACILITIES</a><a href="#">CONTACT</a>
</nav>
<div class="abs dots"><span></span><span></span><span class="on"></span><span></span><span></span></div>
<h1 class="abs hero-title">Store Space Meadowvale</h1>
<div class="abs btn hero-btn">Read More</div>

<section class="abs welcome">
  <h3>WELCOME TO</h3>
  <h2>PARC VELDHOEVE</h2>
  <p>Lorem ipsum dolor sit amet, consectetur adipiscing elit. Aenean eui smod bibendum laoreet. Proin gravida dolor sit amet lacus accumsan et viverra justo commodo.similique sunt in culpa qui officia deserunt mollitia animi, id est laborum et dolorum fuga. Et harum quidem rerum facilis.</p>
  <div class="btn">Read More</div>
</section>
<div class="abs welcome-photo" role="img" aria-label="Photo of a white chalet beside a pond surrounded by trees"></div>

<h2 class="abs section-title">Recente Chalets</h2>

<article class="abs card" style="left:108px">
  <div class="photo" role="img" aria-label="Photo of a grey chalet with a garden"></div>
  <span class="tag rec">Aanbevolen</span><span class="tag type">Huren</span>
  <h4>Kavel 190</h4><div class="price">€ 350 per maand</div>
  <div class="stats" style="top:166px">▭ 1 &nbsp;&nbsp; ▭ 3 &nbsp;&nbsp; ▭ 105 000,00 m²</div>
  <span class="more" style="top:165px">lees meer</span>
  <hr><div class="author"><i></i>admin</div>
  <div class="actions"><span></span><span></span><span></span></div>
</article>
<article class="abs card" style="left:312px">
  <div class="photo" role="img" aria-label="Photo of a white chalet by the water"></div>
  <span class="tag rec">Aanbevolen</span><span class="tag type" style="right:58px">Kopen</span><span class="tag" style="right:18px">Verkocht</span>
  <h4>Kavel 233</h4><div class="price">€ 205.000</div>
  <div class="note">Ook een mooie chalet.</div>
  <div class="stats" style="top:178px">▭ 1 &nbsp;&nbsp; ▭ 1 &nbsp;&nbsp; ▭ 130,00 m²</div>
  <span class="more" style="top:177px">lees meer</span>
  <hr><div class="author"><i></i>admin</div>
  <div class="actions"><span></span><span></span><span></span></div>
</article>
<article class="abs card" style="left:516px">
  <div class="photo" role="img" aria-label="Photo of a wooden chalet" style="background:linear-gradient(180deg,#b6b4a8 0%,#8a5a32 50%,#4a4a44 100%)"></div>
  <span class="tag rec">Aanbevolen</span><span class="tag type">Kopen</span>
  <h4>Kavel 236</h4><div class="price">€ 195.000</div>
  <div class="note">Prachtige locatie incl. video!</div>
  <div class="stats" style="top:178px">▭ 3 &nbsp;&nbsp; ▭ 2 &nbsp;&nbsp; ▭ 100,00 m²</div>
  <span class="more" style="top:177px">lees meer</span>
  <hr><div class="author"><i style="background:#ccc"></i>Naam Achternaam</div>
  <div class="actions"><span></span><span></span><span></span></div>
</article>

<footer class="abs footer">
  <h5 style="left:105px">Contact</h5>
  <div class="contact">
    <div><i></i><span>Beukenlaan 14b<br>4000 AB Hoevedorp</span></div>
    <div><i></i>0300 - 12 34 56</div>
    <div><i></i>0300 - 12 34 78</div>
    <div><i></i>info@parcveldhoeve.example</div>
    <div><i></i>parcVeldhoeveChat</div>
    <div><i></i>http://parc-veldhoeve.example</div>
  </div>
  <h5 style="left:309px">Nieuwe Chalets</h5>
  <div class="mini" style="top:46px"><div class="thumb" role="img" aria-label="Chalet thumbnail"></div><div>Kavel 190<em>€ 350 per maand</em></div></div>
  <div class="mini" style="top:91px"><div class="thumb" role="img" aria-label="Chalet thumbnail"></div><div>Kavel 233<em>€ 205.000</em></div></div>
  <h5 style="left:513px">Sociale media</h5>
  <div class="soc"><span></span><span></span><span></span><span></span><span></span><span></span><span></span><span></span><span></span><span></span><span></span><span></span></div>
</footer>
<div class="abs bottom">Copyright 2018 | Parc Veldhoeve</div>
</body>
</html>
```